ultra-minimalist business card

front (black background, matte):

tarik b. hosseny
writer | photographer
get@tarikhosseny.com

back (white background, matte):

a picture speaks a thousand words;
a word draws a thousand pictures.

www.tarikhosseny.com

all text should be small (white or silver - as long as it shows against the black - on the front; black or gray - as long as it shows against the white - on the back).

feel free to get creative in terms of arrangement, alignment, and font type, but remember, the overall style is minimalist, so nothing too fancy, please.

thanks.

```html
<!DOCTYPE html>
<html lang="en">
<head>
<meta charset="utf-8">
<title>tarik b. hosseny — business card</title>
<link href="https://fonts.googleapis.com/css2?family=Roboto+Slab:wght@400;700&display=swap" rel="stylesheet">
<style>
  :root {
    --page: #ffffff;
    --card-front: #0b0b0c;
    --card-back: #ffffff;
    --card-border: #6a6a6a;
    --ink-light: #e6e6e6;
    --ink-silver: #c9c9c9;
    --ink-dark: #3a3a3a;
    --accent: #b3201f;
  }
  * { margin: 0; padding: 0; box-sizing: border-box; }
  html, body {
    width: 1200px;
    height: 1061px;
    overflow: hidden;
    background: var(--page);
    font-family: "Roboto Slab", Georgia, serif;
  }
  .canvas {
    position: relative;
    width: 1200px;
    height: 1061px;
  }
  .card {
    position: absolute;
    width: 676px;
    height: 388px;
  }
  .card--front {
    left: 108px;
    top: 91px;
    background: var(--card-front);
  }
  .card--back {
    left: 401px;
    top: 457px;
    background: var(--card-back);
    border: 2px solid var(--card-border);
  }
  .identity {
    position: absolute;
    left: 336px;
    top: 146px;
    padding-left: 13px;
    border-left: 3px solid var(--accent);
    font-size: 18px;
    line-height: 27px;
    color: var(--ink-silver);
  }
  .identity__name {
    font-weight: 700;
    color: var(--ink-light);
  }
  .back-content {
    position: absolute;
    inset: 0;
    display: flex;
    flex-direction: column;
    align-items: center;
    text-align: center;
    color: var(--ink-dark);
    font-size: 17px;
  }
  .quote {
    margin-top: 92px;
    line-height: 27px;
  }
  .divider {
    width: 98px;
    height: 3px;
    margin-top: 43px;
    background: var(--accent);
  }
  .website {
    margin-top: 59px;
    line-height: 27px;
  }
</style>
</head>
<body>
  <main class="canvas">
    <section class="card card--front" aria-label="Card front">
      <div class="identity">
        <p class="identity__name">tarik b. hosseny</p>
        <p class="identity__role">writer | photographer</p>
        <p class="identity__email">get@tarikhosseny.com</p>
      </div>
    </section>
    <section class="card card--back" aria-label="Card back">
      <div class="back-content">
        <p class="quote">a picture speaks a thousand words;<br>a word draws a thousand pictures.</p>
        <span class="divider"></span>
        <p class="website">www.tarikhosseny.com</p>
      </div>
    </section>
  </main>
</body>
</html>
```